New image for luxury travel blog

I would like to refresh my blog and social media platforms and would require a new design concept for lilyfarwander.net. I will require the following:

- Top banner for website using current size
- Similar imagery for Facebook Page, Twitter Profile, Google Plus (page and personal profile)
- New profile photo (for each social platform) in appropriate sizes for each platform (with white round shape as I currently have), and 2-3 larger options (500x500, 250x250px)
- Artwork for business card (pavex.net)
- A square logo (based on image defined) for Lily Far Wander Notes (that can be used as an ad of just when I need a logo of the blog)
- Copy to use - Lily Far Wander Notes - a luxury travel blog by Beth Kowal Trenholm.
- Current tagline 'Pack light. Meet kin. Wear heels.' should also be used, but suggestions welcome.
- I am partial to a shade of blue

Feel free to use any photo you can find on my blog at http://lilyfarwander.net which you may find appropriate.

```html
<!DOCTYPE html>
<html lang="en">
<head>
<meta charset="utf-8">
<title>Lily Far Wander Notes – Banner</title>
<link rel="stylesheet" href="https://fonts.googleapis.com/css2?family=Raleway:wght@400&family=Oswald:wght@500&display=swap">
<style>
  :root {
    --blue-deep: #1c86c9;
    --blue-mid: #25aee6;
    --blue-light: #7fd2f1;
    --photo-dark: #3a3236;
    --photo-warm: #8a6a5c;
    --ink-white: #ffffff;
    --ink-soft: #eaf8fe;
  }
  html, body {
    margin: 0;
    padding: 0;
    overflow: hidden;
    background: #ffffff;
  }
  .banner {
    position: relative;
    width: 1200px;
    height: 104px;
    overflow: hidden;
    background: linear-gradient(90deg, var(--blue-deep) 0%, var(--blue-mid) 35%, var(--blue-mid) 65%, var(--blue-light) 100%);
  }
  .banner__portrait {
    position: absolute;
    left: 0;
    top: 0;
    width: 320px;
    height: 104px;
    background: linear-gradient(90deg, var(--photo-dark) 0%, var(--photo-warm) 50%, rgba(37,174,230,0) 100%);
  }
  .banner__landmark {
    position: absolute;
    left: 352px;
    top: 4px;
    width: 48px;
    height: 100px;
    background: linear-gradient(180deg, rgba(255,255,255,0.1), rgba(255,255,255,0.45));
  }
  .banner__title {
    position: absolute;
    left: 425px;
    top: 14px;
    margin: 0;
    font-family: "Raleway", sans-serif;
    font-weight: 400;
    font-size: 40px;
    line-height: 1;
    color: var(--ink-white);
    white-space: nowrap;
  }
  .banner__tagline {
    position: absolute;
    left: 437px;
    top: 68px;
    margin: 0;
    font-family: "Oswald", sans-serif;
    font-weight: 500;
    font-size: 15px;
    line-height: 20px;
    letter-spacing: 0.06em;
    text-transform: uppercase;
    color: var(--ink-soft);
    white-space: nowrap;
  }
  .banner__byline {
    position: absolute;
    right: 14px;
    top: 68px;
    margin: 0;
    font-family: "Raleway", sans-serif;
    font-weight: 400;
    font-size: 16px;
    line-height: 20px;
    color: var(--ink-white);
    white-space: nowrap;
  }
</style>
</head>
<body>
  <header class="banner">
    <div class="banner__portrait" role="img" aria-label="Portrait photo of the blogger smiling"></div>
    <div class="banner__landmark" role="img" aria-label="Faint silhouette of a Paris tower"></div>
    <h1 class="banner__title">Lily Far Wander Notes</h1>
    <p class="banner__tagline">Pack light. Meet kin. Wear heels.</p>
    <p class="banner__byline">A luxury travel blog by Beth Kowal Trenholm</p>
  </header>
</body>
</html>
```